banner ad

We're looking for a banner similar to the one shown on the attached file. The same 4 keywords, the same text up top, but with new formatting, design and perhaps color scheme. Looking for something to catch people's attention that will stand out on this particular page shown in the attached image. Our goal is to find a banner with a better click through rate than the current version.

```html
<!DOCTYPE html>
<html lang="en">
<head>
<meta charset="utf-8">
<title>Blood Sugar Banner Concepts</title>
<link rel="stylesheet" href="https://fonts.googleapis.com/css2?family=Arimo:wght@400;500&display=swap">
<style>
  :root {
    --page: #ffffff;
    --red: #c63d30;
    --red-dark: #7a1510;
    --cell-tone: rgba(150, 24, 16, 0.55);
    --glow-text: #f7aa9e;
    --plain-text: #ffffff;
  }
  * { margin: 0; padding: 0; box-sizing: border-box; }
  html, body {
    width: 1200px; height: 711px; overflow: hidden;
    background: var(--page);
  }
  .canvas { position: relative; width: 1200px; height: 711px; }
  .banner {
    position: absolute; left: 131px; width: 948px; height: 216px;
    overflow: hidden;
    background: linear-gradient(to right,
      var(--red) 0%, var(--red-dark) 11%, var(--red) 17%,
      var(--red) 32%, var(--red-dark) 44%, var(--red) 52%,
      var(--red) 60%, var(--red-dark) 67%, var(--red) 74%,
      var(--red) 80%, var(--red-dark) 87%, var(--red) 95%, var(--red) 100%);
    font-family: "Arimo", Arial, sans-serif;
  }
  .banner--glow { top: 141px; box-shadow: 0 0 14px rgba(200, 80, 70, 0.35); }
  .banner--clean { top: 376px; }
  .cells-art {
    position: absolute; width: 160px; height: 180px;
    background: radial-gradient(ellipse at center, var(--cell-tone) 0%, rgba(150, 24, 16, 0) 70%);
  }
  .cells-art--left { left: 10px; top: 26px; }
  .cells-art--right { left: 760px; top: 24px; }
  .keyword {
    position: absolute; transform: translate(-50%, -50%);
    white-space: nowrap; font-size: 26.5px; line-height: 1;
  }
  .banner--glow .keyword {
    color: var(--glow-text); font-weight: 500; letter-spacing: -0.4px;
    text-shadow: 0 0 1px #ffd6cf, 0 0 3px rgba(255, 200, 190, 0.6);
  }
  .banner--clean .keyword { color: var(--plain-text); font-weight: 400; }
  .k1 { left: 278px; top: 72px; }
  .k2 { left: 588px; top: 85px; }
  .k3 { left: 279px; top: 147px; }
  .k4 { left: 647px; top: 163px; }
</style>
</head>
<body>
<main class="canvas">
  <section class="banner banner--glow">
    <div class="cells-art cells-art--left" role="img" aria-label="Illustration of floating red blood cells"></div>
    <div class="cells-art cells-art--right" role="img" aria-label="Illustration of floating red blood cells"></div>
    <span class="keyword k1">Blood Glucose</span>
    <span class="keyword k2">Blood Sugar Level Chart</span>
    <span class="keyword k3">Normal Blood Sugar Range</span>
    <span class="keyword k4">What Is Normal Blood Sugar</span>
  </section>
  <section class="banner banner--clean">
    <div class="cells-art cells-art--left" role="img" aria-label="Illustration of floating red blood cells"></div>
    <div class="cells-art cells-art--right" role="img" aria-label="Illustration of floating red blood cells"></div>
    <span class="keyword k1">Blood Glucose</span>
    <span class="keyword k2">Blood Sugar Level Chart</span>
    <span class="keyword k3">Normal Blood Sugar Range</span>
    <span class="keyword k4">What Is Normal Blood Sugar</span>
  </section>
</main>
</body>
</html>
```